Business Card Designs

Looking to design a 3.5" x 2" standard business card for our employees.
The design needs to be sleek, simple, and modern. We would like our logo (attached) to be incorporated, but not in that colour, rather an outline of the logo in either gold or silver (whichever looks better).

Modern and Simple is what we are looking for, but be creative in incorporating the logo.

```html
<!DOCTYPE html>
<html lang="en">
<head>
<meta charset="utf-8">
<title>Harbourline Suites – Business Card</title>
<link href="https://fonts.googleapis.com/css2?family=Montserrat:wght@700;800&family=Open+Sans:wght@400;600&display=swap" rel="stylesheet">
<style>
  :root {
    --page: #e4e6e7;
    --card-white: #ffffff;
    --card-mist: #eef1f1;
    --teal: #4e8c88;
    --teal-soft: #a6cccb;
    --gold: #c8b57a;
    --ink: #3a3f42;
    --rule: #55595c;
  }
  * { box-sizing: border-box; margin: 0; padding: 0; }
  html, body { width: 1200px; height: 900px; overflow: hidden; }
  body {
    background: var(--page);
    font-family: "Open Sans", Arial, sans-serif;
    color: var(--ink);
    position: relative;
  }
  .card {
    position: absolute;
    left: 250px;
    width: 700px;
    height: 400px;
    border-radius: 34px;
    box-shadow: 0 10px 28px rgba(0,0,0,.18);
    overflow: hidden;
  }
  .card--back {
    top: 35px;
    background: radial-gradient(ellipse at 55% 48%, #f6f7f7 0%, #e3eeee 45%, var(--teal-soft) 100%);
    display: flex;
    align-items: center;
    justify-content: center;
  }
  .card--front {
    top: 465px;
    background: linear-gradient(180deg, var(--card-white) 0%, var(--card-mist) 100%);
  }
  .brand-name {
    font-family: "Montserrat", Arial, sans-serif;
    font-weight: 800;
    color: var(--teal);
    text-transform: uppercase;
    letter-spacing: 2px;
  }
  .card--back .brand-name { font-size: 34px; }
  .brand-lockup {
    position: absolute;
    left: 60px;
    top: 60px;
    display: flex;
    align-items: center;
    gap: 14px;
  }
  .brand-lockup .brand-mark {
    width: 22px; height: 22px;
    background: var(--teal);
  }
  .brand-lockup .brand-name { font-size: 22px; line-height: 1.15; }
  .person {
    position: absolute;
    right: 318px;
    top: 250px;
    text-align: right;
  }
  .person__name {
    font-family: "Montserrat", Arial, sans-serif;
    font-weight: 800;
    font-size: 24px;
    color: var(--gold);
    letter-spacing: 1px;
  }
  .person__role { font-size: 17px; color: var(--ink); margin-top: 2px; }
  .divider {
    position: absolute;
    left: 398px;
    top: 170px;
    width: 1.5px;
    height: 150px;
    background: var(--rule);
  }
  .contacts {
    position: absolute;
    left: 418px;
    top: 168px;
    list-style: none;
    font-size: 17px;
    line-height: 1.2;
  }
  .contacts li { display: flex; align-items: flex-start; gap: 10px; margin-bottom: 9px; }
  .contacts svg { width: 17px; height: 17px; flex: none; margin-top: 2px; fill: var(--teal); }
</style>
</head>
<body>
  <section class="card card--back" aria-label="Card back">
    <span class="brand-name">Harbourline Suites</span>
  </section>

  <section class="card card--front" aria-label="Card front">
    <div class="brand-lockup">
      <span class="brand-mark"></span>
      <span class="brand-name">Harbourline<br>Suites</span>
    </div>

    <div class="person">
      <p class="person__name">EVAN MARLOW</p>
      <p class="person__role">Director</p>
    </div>

    <div class="divider"></div>

    <ul class="contacts">
      <li>
        <svg viewBox="0 0 24 24" aria-hidden="true"><path d="M6.6 10.8a15 15 0 0 0 6.6 6.6l2.2-2.2a1 1 0 0 1 1-.25 11.4 11.4 0 0 0 3.6.57 1 1 0 0 1 1 1V20a1 1 0 0 1-1 1A17 17 0 0 1 3 4a1 1 0 0 1 1-1h3.5a1 1 0 0 1 1 1c0 1.25.2 2.45.57 3.6a1 1 0 0 1-.25 1z"/></svg>
        <span>555-210-4470</span>
      </li>
      <li>
        <svg viewBox="0 0 24 24" aria-hidden="true"><path d="M3 5h18a1 1 0 0 1 1 1v12a1 1 0 0 1-1 1H3a1 1 0 0 1-1-1V6a1 1 0 0 1 1-1zm9 7.2L20 7H4z"/></svg>
        <span>hello@hlsuites.com</span>
      </li>
      <li>
        <svg viewBox="0 0 24 24" aria-hidden="true"><path d="M12 2a10 10 0 1 0 0 20 10 10 0 0 0 0-20zm6.9 9h-3a15 15 0 0 0-1.3-6 8 8 0 0 1 4.3 6zM12 4.1c.9 1.2 1.7 3.6 1.9 6.9h-3.8c.2-3.3 1-5.7 1.9-6.9zM9.4 5a15 15 0 0 0-1.3 6h-3a8 8 0 0 1 4.3-6zM5.1 13h3a15 15 0 0 0 1.3 6 8 8 0 0 1-4.3-6zm6.9 6.9c-.9-1.2-1.7-3.6-1.9-6.9h3.8c-.2 3.3-1 5.7-1.9 6.9zm2.6-.9a15 15 0 0 0 1.3-6h3a8 8 0 0 1-4.3 6z"/></svg>
        <span>www.hlsuites.com</span>
      </li>
      <li>
        <svg viewBox="0 0 24 24" aria-hidden="true"><path d="M12 2a7 7 0 0 0-7 7c0 5 7 13 7 13s7-8 7-13a7 7 0 0 0-7-7zm0 9.5A2.5 2.5 0 1 1 12 6.5a2.5 2.5 0 0 1 0 5z"/></svg>
        <span>12 sample street<br>sample town 0000</span>
      </li>
    </ul>
  </section>
</body>
</html>
```